ultra-minimalist business card

front (black background, matte):

tarik b. hosseny
writer | photographer
get@tarikhosseny.com

back (white background, matte):

a picture speaks a thousand words;
a word draws a thousand pictures.

www.tarikhosseny.com

all text should be small (white or silver - as long as it shows against the black - on the front; black or gray - as long as it shows against the white - on the back).

feel free to get creative in terms of arrangement, alignment, and font type, but remember, the overall style is minimalist, so nothing too fancy, please.

thanks.

```html
<!DOCTYPE html>
<html lang="en">
<head>
<meta charset="utf-8">
<title>Tarik B. Hosseny — Business Card Back</title>
<link rel="stylesheet" href="https://fonts.googleapis.com/css2?family=Comic+Neue:wght@400&family=Roboto+Condensed:wght@700&display=swap">
<style>
  :root {
    --card-bg: #ffffff;
    --ink: #000000;
  }
  html, body {
    margin: 0;
    padding: 0;
    width: 1200px;
    height: 632px;
    overflow: hidden;
    background: var(--card-bg);
  }
  .card-back {
    position: relative;
    width: 1200px;
    height: 632px;
    background: var(--card-bg);
    color: var(--ink);
  }
  .quote {
    position: absolute;
    top: 131px;
    left: 0;
    width: 100%;
    margin: 0;
    text-align: center;
    font-family: "Comic Neue", "Comic Sans MS", cursive;
    font-weight: 400;
    font-size: 56px;
    line-height: 63px;
    letter-spacing: 0;
  }
  .quote-line {
    display: block;
  }
  .website {
    position: absolute;
    top: 454px;
    left: 0;
    width: 100%;
    margin: 0;
    text-align: center;
    font-family: "Roboto Condensed", "Arial Narrow", sans-serif;
    font-weight: 700;
    font-size: 49px;
    line-height: 54px;
  }
</style>
</head>
<body>
  <main class="card-back">
    <p class="quote">
      <span class="quote-line">a picture speaks</span>
      <span class="quote-line">a thousand words;</span>
      <span class="quote-line">a word draws</span>
      <span class="quote-line">a thousand pictures.</span>
    </p>
    <p class="website">www.tarikhosseny.com</p>
  </main>
</body>
</html>
```